Window Cleaning Service

I want to design a postcard for my window cleaning business in Las Vegas, Nevada. I think it should include... specials staring at $95, senior and military discounts, that we are licensed, insured and bonded and have strong call to actions. Here is a link to my website for ideas (you may want to check out the services and specials pages for more information on the business, that may help) http://www.brightpanewashers.example/

Also, I'm looking for 2 sided design in full color and to use the same color scheme as my logo. If you would lime to speak to me call me anytime at 555-384-9127 or email at info@brightpanewashers.example

Thank you in advance,
Marcus

Target Market(s)

residential home owners

Industry/Entity Type

Window Cleaning

Requirements
Must have
• Special's starting at $95
• Fully licensed, Insured, and Bonded
Nice to have
• Strong call to actions
• "Excellent customer service backed by great pricing"
• Also, our secondary service is solar panel/solar array cleaning but 90% of the business is window cleaning
Should not have
• home cleaning service, We are window cleaners not a maid service. I don't want anyone to think its a maid service/house cleaning service

```html
<!DOCTYPE html>
<html lang="en">
<head>
<meta charset="utf-8">
<title>Bright Pane Washers – Postcard</title>
<link href="https://fonts.googleapis.com/css2?family=Roboto+Condensed:ital,wght@0,400;0,700;1,400&family=Delius&display=swap" rel="stylesheet">
<style>
  :root{
    --blue:#1d5fa9;
    --blue-dark:#0e4685;
    --blue-light:#4d8fd0;
    --sky:#eaf3fb;
    --green:#7cbb3c;
    --grey:#6a6a6a;
    --grey-dark:#555;
    --white:#fff;
    --bg:#e9e6e2;
  }
  *{box-sizing:border-box;margin:0;padding:0}
  html,body{width:1200px;height:840px;overflow:hidden;background:var(--bg)}
  .canvas{position:relative;width:1200px;height:840px}
  .card{position:absolute;width:518px;height:670px;background:linear-gradient(#e6f1fb 0%,#fff 30%,#fff 100%);box-shadow:0 4px 14px rgba(0,0,0,.25);overflow:hidden;font-family:"Roboto Condensed",sans-serif}
  .card--front{left:58px;top:55px}
  .card--back{left:634px;top:130px}
  .brand{position:absolute;z-index:2;left:18px;top:62px;display:flex;align-items:center;gap:8px;font-family:"Delius",cursive;font-size:24px;color:var(--blue);white-space:nowrap}
  .card--back .brand{top:58px}
  .brand__dot{width:14px;height:14px;border-radius:50%;background:var(--green)}
  .credentials{position:absolute;z-index:2;right:14px;top:28px;width:200px;text-align:center;font-family:"Delius",cursive;font-size:20px;line-height:27px;color:var(--grey-dark)}
  .band{position:absolute;left:0;width:518px}
  .badge{position:absolute;z-index:3;border-radius:50%;display:flex;flex-direction:column;align-items:center;justify-content:center;text-align:center;font-family:"Delius",cursive}
  .badge--special{left:22px;top:175px;width:142px;height:142px;background:#fff;border:6px solid var(--green);box-shadow:0 0 0 3px #fff,0 0 0 5px var(--green);color:var(--grey-dark);font-size:19px;line-height:21px}
  .badge--special .price{font-size:32px;line-height:34px}
  .badge--discount{left:372px;top:92px;width:118px;height:118px;background:#eef3f8;border:5px solid var(--blue-light);color:var(--grey-dark);font-size:15px;line-height:18px;transform:rotate(15deg)}
  .small{font-size:9px;line-height:10px}
  .headline{position:absolute;left:0;width:100%;top:372px;text-align:center;font-weight:700;font-size:25px;color:var(--blue)}
  .subhead{position:absolute;left:22px;top:416px;font-size:18px;color:var(--green)}
  .services{position:absolute;top:448px;list-style:none;width:242px;font-size:12px;line-height:14px;color:var(--grey)}
  .services--left{left:18px}
  .services--right{left:268px}
  .services li{position:relative;padding-left:16px;margin-bottom:6px}
  .services li::before{content:"";position:absolute;left:0;top:2px;width:10px;height:10px;border-radius:50%;background:var(--green)}
  .promise{font-family:"Delius",cursive;color:var(--blue);text-align:center;position:absolute;z-index:2}
  .card--front .promise{left:268px;top:572px;width:235px;font-size:15px;line-height:23px}
  .card--back .promise{left:240px;top:362px;width:268px;font-size:19px;line-height:28px}
  .cta{position:absolute;left:0;bottom:0;width:100%;height:46px;background:linear-gradient(var(--blue-light),var(--blue-dark));display:flex;align-items:center;justify-content:center;gap:12px;color:var(--white);font-family:"Roboto Condensed",sans-serif}
  .cta__text{font-size:17px}
  .cta__phone{font-size:25px;font-weight:700}
  .tagline{position:absolute;z-index:2;left:110px;top:196px;width:300px;text-align:center;font-family:"Delius",cursive;color:var(--white);font-size:18px;line-height:26px}
  .portrait{position:absolute;z-index:2;left:30px;top:243px;width:174px;height:174px;border-radius:50%;border:5px solid #fff;background:linear-gradient(160deg,#9a4a3a,#6f6a5e 55%,#3c4a5a);box-shadow:0 2px 6px rgba(0,0,0,.3)}
  .checklist{position:absolute;left:18px;top:433px;width:490px;list-style:none}
  .checklist li{position:relative;padding-left:20px;margin-bottom:8px;font-size:12px;line-height:14px;color:var(--grey)}
  .checklist svg{position:absolute;left:0;top:1px}
  .checklist b{font-size:16px;color:var(--blue);font-weight:400}
  .checklist i{font-style:italic}
  .contact{position:absolute;left:0;top:562px;width:100%;text-align:center;font-family:"Delius",cursive;font-size:14.5px;line-height:19px;color:var(--blue)}
</style>
</head>
<body>
<div class="canvas">

  <section class="card card--front">
    <svg class="band" style="top:95px;height:300px" viewBox="0 0 518 300" preserveAspectRatio="none">
      <defs>
        <linearGradient id="frontPhoto" x1="0" y1="0" x2="1" y2="1">
          <stop offset="0" stop-color="#bcd9f1"/><stop offset=".5" stop-color="#3f7fc4"/><stop offset="1" stop-color="#1c5ba3"/>
        </linearGradient>
      </defs>
      <rect role="img" aria-label="Photo of a squeegee wiping soapy water from a window" x="0" y="20" width="518" height="260" fill="url(#frontPhoto)"/>
      <path d="M0 78 C160 30 330 80 518 36 V0 H0Z" fill="#1d5fa9"/>
      <path d="M0 70 C160 22 330 70 518 28 V0 H0Z" fill="#7cbb3c"/>
      <path d="M0 62 C160 16 330 62 518 22 V0 H0Z" fill="#e8f2fb"/>
      <path d="M0 236 C150 270 340 200 518 250 V300 H0Z" fill="#7cbb3c"/>
      <path d="M0 248 C150 282 340 214 518 262 V300 H0Z" fill="#1d5fa9"/>
      <path d="M0 258 C150 292 340 226 518 272 V300 H0Z" fill="#fff"/>
    </svg>

    <div class="brand"><span class="brand__dot"></span>Bright Pane Washers</div>
    <p class="credentials">Fully licensed, Insured, and Bonded</p>

    <div class="badge badge--special">
      <span>EXTERIOR</span><span>SPECIALS</span><span>staring at</span><span class="price">$95</span><span class="small">can not combine</span>
    </div>

    <h1 class="headline">TOP-NOTCH WINDOW CLEANING SERVICE</h1>
    <h2 class="subhead">Residential and Commercial Cleaning</h2>

    <ul class="services services--left">
      <li>Dryer Vent Cleaning – Prevent Fires and Save on Utilites</li>
      <li>Solar Panel Cleaning – Increase Productivity</li>
      <li>Detailed Cleaning of all Windows Inside and Out</li>
      <li>72 Hour Rain Guarantee</li>
      <li>Sills and Tracks Cleaned</li>
      <li>Screens Cleaned – 3 step process that includes screen majic</li>
    </ul>
    <ul class="services services--right">
      <li>Glass and Mirror Cleaning</li>
      <li>Hard Water &amp; Lime Spot Removal- Sparkling Clean Showers</li>
      <li>Specially Formulated Soap for Lasting Shine</li>
      <li>Chandeliers and Lighting Fixtures Hand Cleaned</li>
      <li>Mess Free – No Drips or Streaks Left Behind</li>
    </ul>

    <p class="promise">Excellent Customer Service<br>Backed By Great Pricing!!!</p>

    <div class="cta">
      <span class="cta__text">Call today for your FREE&nbsp; ESTIMATE</span>
      <svg width="30" height="30" viewBox="0 0 30 30" aria-hidden="true"><circle cx="15" cy="15" r="13" fill="none" stroke="#fff" stroke-width="2"/><path d="M10 8 l3 0 1 4 -2 1.5 c1 2.5 2.5 4 4.5 4.5 l1.5-2 4 1 0 3 c-7 1-12.5-5-12-12z" fill="#fff"/></svg>
      <span class="cta__phone">555-218-4630</span>
    </div>
  </section>

  <section class="card card--back">
    <svg class="band" style="top:95px;height:280px" viewBox="0 0 518 280" preserveAspectRatio="none">
      <defs>
        <linearGradient id="backPhoto" x1="0" y1="0" x2="1" y2="1">
          <stop offset="0" stop-color="#cfe3f5"/><stop offset=".45" stop-color="#5b95d0"/><stop offset="1" stop-color="#2a68ad"/>
        </linearGradient>
      </defs>
      <rect role="img" aria-label="Photo of a squeegee clearing a soapy window" x="0" y="10" width="518" height="260" fill="url(#backPhoto)"/>
      <path d="M0 40 C170 18 340 30 518 14 V0 H0Z" fill="#1d5fa9"/>
      <path d="M0 32 C170 10 340 22 518 6 V0 H0Z" fill="#7cbb3c"/>
      <path d="M0 25 C170 4 340 15 518 0 V0 H0Z" fill="#e8f2fb"/>
      <path d="M0 240 C180 210 340 230 518 210 V280 H0Z" fill="#1d5fa9"/>
      <path d="M0 252 C180 222 340 242 518 222 V280 H0Z" fill="#7cbb3c"/>
      <path d="M0 262 C180 234 340 252 518 234 V280 H0Z" fill="#fff"/>
    </svg>

    <div class="brand">Bright Pane Washers<span class="brand__dot"></span></div>
    <p class="credentials">Fully licensed, Insured, and Bonded</p>

    <div class="badge badge--discount">
      <span>Senior And</span><span>Military</span><span>DISCOUNTS!</span><span class="small">can not combine</span>
    </div>

    <p class="tagline">Family Owned And Operated,<br>We Care!</p>

    <div class="portrait" role="img" aria-label="Photo of the owner standing with his two sons"></div>

    <p class="promise">Excellent Customer Service<br>Backed By Great Pricing!!!</p>

    <ul class="checklist">
      <li><svg width="14" height="14" viewBox="0 0 14 14" aria-hidden="true"><rect x="1" y="2" width="11" height="11" fill="none" stroke="#7cbb3c" stroke-width="1.5"/><path d="M3 7 l3 3 7-8" fill="none" stroke="#7cbb3c" stroke-width="2"/></svg><b>WINDOW CLEANING</b> <i>We use eco-friendly green solutions and have exceptional attention to detail. Your satisfaction is our #1 priority.</i></li>
      <li><svg width="14" height="14" viewBox="0 0 14 14" aria-hidden="true"><rect x="1" y="2" width="11" height="11" fill="none" stroke="#7cbb3c" stroke-width="1.5"/><path d="M3 7 l3 3 7-8" fill="none" stroke="#7cbb3c" stroke-width="2"/></svg><b>SOLAR PANEL CLEANING</b> <i>Increase productivity and save money. Our cleaning process is safe and effective and we will take the time to make sure it's done properly.</i></li>
      <li><svg width="14" height="14" viewBox="0 0 14 14" aria-hidden="true"><rect x="1" y="2" width="11" height="11" fill="none" stroke="#7cbb3c" stroke-width="1.5"/><path d="M3 7 l3 3 7-8" fill="none" stroke="#7cbb3c" stroke-width="2"/></svg><b>DRYER VENT CLEANING</b> <i>Clothing dryers cause 15k fires a year. Protect your home and save money. Schedule your dyer vent cleaning today.</i></li>
    </ul>

    <p class="contact">Please Contact Us:<br>p:&nbsp; 555-218-4630&nbsp; e:&nbsp; info@brightpanewashers.example<br>www.brightpanewashers.example</p>

    <div class="cta">
      <span class="cta__text">Call today for your FREE&nbsp; ESTIMATE</span>
      <svg width="30" height="30" viewBox="0 0 30 30" aria-hidden="true"><circle cx="15" cy="15" r="13" fill="none" stroke="#fff" stroke-width="2"/><path d="M10 8 l3 0 1 4 -2 1.5 c1 2.5 2.5 4 4.5 4.5 l1.5-2 4 1 0 3 c-7 1-12.5-5-12-12z" fill="#fff"/></svg>
      <span class="cta__phone">555-218-4630</span>
    </div>
  </section>

</div>
</body>
</html>
```